Vibrational sessions for Healing

I am looking for a business card that is unique that sends a message to open minded folk that vibrational healing is paramount to their life journey and if they are open to this idea it can move mountains for them! All they have to have is a belief! IT is as simple as that!
Meadow Lantern is the company based in Western Australia, and as the energy that we are working with is everywhere, it is universal, so to speak!
The design we would like to see is of light shades of rainbow colours radiating light and energy so whatever you think is appropriate to send the message that if you want to move on in you life in a down to earth fashion, then this is the way for folk to find themselves! Something completely different and out of the ordinary and affordable to most, quirky in nature, but completely out of this world idea that will hit the masses by storm!
A website is being developed as we speak, so a new method of healing will be upon us very soon in an unusual fasion, so to speak!
Looking forward to your wonderful bright ideas so we an get started on this venture to enlighten many folk that are on the brink of making a truthful life for themselves.
Warm Regards,
Ruth

Reason: Hi there, I am new to this game and as this is my first time advertising with ArtHuddle, I was unaware of the time it takes to submit replies and answers to the designers. As I posted the add early in the week, I feel that those first 2 days were just acknowledging designers and sending off extra information for the deign of the card. I would appreciate an extension of time. Thank you. Ruth

Business

Vibrational Healing, Ruth Tallowby, Coralbay WA 6537, Practitioner

Abstract Logo
• As this is energy we are talking about, a design that is wispy with a hint of something happening on the card, pastel shades but can be a bold colour somewhere to be a feature but not to striking. Also a vague hint of a clothed body (male or female or both, in dress or suit whatever, casual is fine, in an abstract form) that is just distinguishable in the background.
I would like a design that makes people look twice at the design and then they can read into what can actually happen for themselves.
I hope all this makes sense. Any questions, please email me for clarification.Thank you all for being part of the project to get this underway! This will happen!

```html
<!DOCTYPE html>
<html lang="en">
<head>
<meta charset="utf-8">
<title>Meadow Lantern – Vibrational Healing</title>
<link rel="stylesheet" href="https://fonts.googleapis.com/css2?family=Arimo:wght@400;700&family=Archivo+Narrow:wght@400;700&display=swap">
<style>
  :root {
    --ink: #111111;
    --paper: #ffffff;
    --warm: #f6b49a;
    --sun: #f5e39a;
    --leaf: #b9dfa2;
    --sea: #9fd3dc;
    --sky: #a9c4ec;
  }
  * { margin: 0; padding: 0; box-sizing: border-box; }
  html, body { width: 667px; height: 1200px; overflow: hidden; background: var(--paper); }
  .card {
    position: relative;
    width: 667px;
    height: 1200px;
    background: var(--paper);
    color: var(--ink);
    text-align: center;
    overflow: hidden;
  }
  .brand-name {
    position: absolute;
    top: 318px;
    width: 100%;
    font-family: "Arimo", Arial, sans-serif;
    font-weight: 400;
    font-size: 58px;
    line-height: 72px;
    letter-spacing: -1px;
  }
  .tagline {
    position: absolute;
    top: 390px;
    width: 100%;
    font-family: "Arimo", Arial, sans-serif;
    font-weight: 400;
    font-size: 58px;
    line-height: 72px;
    letter-spacing: -0.5px;
    color: #222222;
  }
  .practitioner {
    position: absolute;
    top: 504px;
    width: 100%;
    font-family: "Arimo", Arial, sans-serif;
    font-weight: 400;
    font-size: 50px;
    line-height: 60px;
    letter-spacing: -0.5px;
  }
  .details {
    position: absolute;
    top: 568px;
    width: 100%;
    list-style: none;
    font-family: "Archivo Narrow", "Arial Narrow", sans-serif;
    font-size: 31px;
    line-height: 46px;
  }
  .details strong { font-weight: 700; }
  .radiance {
    position: absolute;
    left: 0;
    top: 830px;
    width: 667px;
    height: 370px;
    background: linear-gradient(90deg, var(--warm) 0%, var(--sun) 30%, var(--leaf) 55%, var(--sea) 78%, var(--sky) 100%);
    -webkit-mask-image: linear-gradient(180deg, rgba(0,0,0,0) 0%, #000 45%);
    mask-image: linear-gradient(180deg, rgba(0,0,0,0) 0%, #000 45%);
  }
</style>
</head>
<body>
  <main class="card">
    <h1 class="brand-name">Meadow Lantern</h1>
    <p class="tagline">Vibrational Healing</p>
    <h2 class="practitioner">Ruth Tallowby</h2>
    <ul class="details">
      <li>Coralbay WA 6537, Practitioner</li>
      <li><strong>mobile:</strong>0412 558 207</li>
      <li><strong>email:</strong> ruth@meadowlantern.net.au</li>
      <li><strong>website:</strong> www.meadowlantern.net.au</li>
      <li><strong>location:</strong> Perth, Western Australia</li>
    </ul>
    <div class="radiance" role="img" aria-label="Soft rainbow-toned decorative area along the bottom edge"></div>
  </main>
</body>
</html>
```